TRELBY Construction Group business card for distribution

A business card detailing our services, with our phone number and email address.
- Groundworks / Foundations / Drainage
- Landscaping / Hard Landscaping / Patios / Decking
- Fencing
The card should include company logo and be in the same colours.

Target Market(s)
Domestic Houses
Industry/Entity Type
Construction
Contact Information for Business Card
Phone Number - 07731 248 905 / 07612093184. Email address: trelbygroup@fenwickmail.com
Font styles to use
Serif
Sans Serif
Colors
F0912C
F2A743
F7CA91
FBE8D2
FDF5EE
Requirements
Must have
- Contact numbers. Photos of past work. Company Logo

Nice to have
- Company Logo

```html
<!DOCTYPE html>
<html lang="en">
<head>
<meta charset="utf-8">
<title>TRELBY Construction Group – Business Card</title>
<link rel="stylesheet" href="https://fonts.googleapis.com/css2?family=Montserrat:wght@500;600;700;800&family=Roboto+Condensed:wght@400&display=swap">
<style>
  :root {
    --stage: #2b2b2b;
    --stage-deep: #141414;
    --card: #000000;
    --panel: #1c1c1c;
    --orange: #f7962d;
    --white: #ffffff;
    --grey: #bdbdbf;
  }
  * { box-sizing: border-box; margin: 0; padding: 0; }
  html, body { width: 1200px; height: 805px; overflow: hidden; }
  body {
    background: radial-gradient(ellipse at 50% 45%, var(--stage), var(--stage-deep));
    font-family: "Montserrat", sans-serif;
    color: var(--white);
    position: relative;
  }
  .card {
    position: absolute;
    top: 247px;
    width: 540px;
    height: 310px;
    background: var(--card);
    border-radius: 22px;
    overflow: hidden;
    box-shadow: 0 18px 40px rgba(0,0,0,.55);
  }
  .card--services { left: 40px; }
  .card--contact { left: 620px; }

  .wordmark {
    display: flex;
    align-items: center;
    gap: 12px;
  }
  .wordmark__square {
    width: 26px; height: 26px;
    background: var(--orange);
    flex: none;
  }
  .wordmark__name {
    font-weight: 700;
    color: var(--white);
    line-height: 1.05;
    letter-spacing: 2px;
  }
  .wordmark__name span { display: block; }
  .wordmark__name .big { font-size: 52px; letter-spacing: 3px; }
  .wordmark__name .small { font-size: 17px; letter-spacing: 3px; margin-top: 4px; }

  /* services side */
  .card--services .wordmark {
    position: absolute;
    top: 58px; left: 0; right: 0;
    justify-content: center;
  }
  .services {
    position: absolute;
    top: 190px; left: 0; right: 0;
    text-align: center;
  }
  .services__title {
    color: var(--orange);
    font-weight: 800;
    font-size: 22px;
    letter-spacing: 1px;
    margin-bottom: 8px;
  }
  .services__list {
    font-family: "Roboto Condensed", sans-serif;
    font-size: 17px;
    line-height: 1.45;
    color: var(--white);
  }

  /* contact side */
  .contact__panel {
    position: absolute;
    top: -30px; right: -30px;
    width: 330px; height: 230px;
    background: var(--panel);
    border-radius: 60px;
  }
  .card--contact .wordmark {
    position: absolute;
    top: 42px; left: 44px;
  }
  .card--contact .wordmark__name .big { font-size: 44px; }
  .card--contact .wordmark__name .small { font-size: 14px; }
  .person {
    position: absolute;
    left: 44px; top: 176px;
  }
  .person__name {
    color: var(--orange);
    font-weight: 800;
    font-size: 24px;
  }
  .person__role {
    font-weight: 600;
    font-size: 15px;
    margin-top: 2px;
  }
  .rule {
    position: absolute;
    left: 44px; right: 44px; top: 240px;
    height: 1.5px;
    background: var(--orange);
  }
  .contact-line {
    position: absolute;
    top: 254px;
    display: flex; align-items: center; gap: 7px;
    font-weight: 500;
    font-size: 13px;
  }
  .contact-line--phone { left: 44px; }
  .contact-line--email { right: 30px; }
  .contact-line svg { width: 15px; height: 15px; flex: none; }
</style>
</head>
<body>
  <section class="card card--services" aria-label="Services side">
    <div class="wordmark">
      <div class="wordmark__square"></div>
      <div class="wordmark__name">
        <span class="big">TRELBY</span>
        <span class="small">CONSTRUCTION GROUP LTD</span>
      </div>
    </div>
    <div class="services">
      <h2 class="services__title">OUR SERVICES</h2>
      <p class="services__list">Groundworks | Foundations | Drainage | Landscaping<br>Hard Landscaping | Decking | Fencing</p>
    </div>
  </section>

  <section class="card card--contact" aria-label="Contact side">
    <div class="contact__panel"></div>
    <div class="wordmark">
      <div class="wordmark__square"></div>
      <div class="wordmark__name">
        <span class="big">TRELBY</span>
        <span class="small">CONSTRUCTION GROUP LTD</span>
      </div>
    </div>
    <div class="person">
      <p class="person__name">Daniel Harrow</p>
      <p class="person__role">Owner</p>
    </div>
    <div class="rule"></div>
    <p class="contact-line contact-line--phone">
      <svg viewBox="0 0 24 24" aria-hidden="true"><path fill="#f7962d" d="M6.6 10.8a15.1 15.1 0 0 0 6.6 6.6l2.2-2.2a1 1 0 0 1 1-.25 11.4 11.4 0 0 0 3.6.57 1 1 0 0 1 1 1V20a1 1 0 0 1-1 1A17 17 0 0 1 3 4a1 1 0 0 1 1-1h3.5a1 1 0 0 1 1 1c0 1.25.2 2.45.57 3.57a1 1 0 0 1-.25 1z"/></svg>
      07731 248 905 / 07612093184
    </p>
    <p class="contact-line contact-line--email">
      <svg viewBox="0 0 24 24" aria-hidden="true"><rect x="2" y="5" width="20" height="14" rx="1.5" fill="#f7962d"/><path d="M3 6.5l9 6.5 9-6.5" fill="none" stroke="#000" stroke-width="1.6"/></svg>
      trelbygroup@fenwickmail.com
    </p>
  </section>
</body>
</html>
```